Simple Recipe eBook

I need the graphic work done for a simple recipe ebook, I have attached all of the required information for it, as well as our company logo. Further company info can be found at velqorith.com

I would like each recipe page to include 2 recipes, each recipe needs to include ingredients, picture, method, and nutritional info.

I would like the style to appear fresh and healthy, with lots of graphics and colours to match.
Please let me know if you need any guidance

Target Market(s)

Females aged from 15-25

Industry/Entity Type

It Company

```html
<!DOCTYPE html>
<html lang="en">
<head>
<meta charset="utf-8">
<title>Velqorith – Recipe Guide Intro</title>
<link rel="stylesheet" href="https://fonts.googleapis.com/css2?family=Open+Sans:wght@600;700&family=Roboto+Slab:wght@500;600&display=swap">
<style>
  :root {
    --teal: #2acbc7;
    --slate: #5a6068;
    --ink: #1f1f1f;
    --wood-light: #e4e4e4;
    --wood-mid: #cfcfcf;
    --wood-dark: #b9b9b9;
    --white: #ffffff;
    --leaf-tone-light: #9fd66a;
    --leaf-tone-dark: #6fae3e;
  }
  * { margin: 0; padding: 0; box-sizing: border-box; }
  html, body { width: 848px; height: 1200px; overflow: hidden; background: var(--white); }
  .page {
    position: relative;
    width: 848px;
    height: 1200px;
    overflow: hidden;
  }
  .wood-backdrop {
    position: absolute;
    inset: 0;
    background:
      linear-gradient(90deg, var(--wood-mid) 0%, var(--wood-light) 18%, var(--wood-mid) 34%, var(--wood-light) 52%, var(--wood-dark) 70%, var(--wood-light) 88%, var(--wood-mid) 100%);
  }
  .side-band {
    position: absolute;
    top: 0;
    left: 758px;
    width: 63px;
    height: 100%;
    background: var(--teal);
  }
  .side-edge {
    position: absolute;
    top: 0;
    left: 824px;
    width: 24px;
    height: 100%;
    background: var(--slate);
  }
  .brand {
    position: absolute;
    top: 8px;
    left: 324px;
    width: 200px;
    text-align: center;
  }
  .brand-mark {
    display: block;
    width: 36px;
    height: 36px;
    margin: 0 auto 6px;
    border-radius: 50%;
    background: var(--slate);
  }
  .brand-name {
    font-family: "Roboto Slab", serif;
    font-weight: 500;
    font-size: 14px;
    letter-spacing: 1.5px;
    color: var(--slate);
  }
  .intro {
    position: absolute;
    top: 172px;
    left: 112px;
    width: 630px;
    text-align: center;
    font-family: "Roboto Slab", serif;
    font-weight: 500;
    font-size: 24px;
    line-height: 40px;
    color: var(--ink);
  }
  .intro p + p { margin-top: 34px; }
  .headline {
    position: absolute;
    inset: 0;
    width: 848px;
    height: 1200px;
  }
  .headline text {
    font-family: "Open Sans", sans-serif;
    font-weight: 600;
    stroke: var(--white);
    stroke-linejoin: round;
    paint-order: stroke;
  }
  .headline .ready, .headline .go { fill: var(--teal); }
  .headline .set { fill: var(--slate); }
  .leaf-photo {
    position: absolute;
    left: 486px;
    top: 956px;
    width: 126px;
    height: 148px;
    background: linear-gradient(160deg, var(--leaf-tone-light), var(--leaf-tone-dark));
  }
</style>
</head>
<body>
  <main class="page">
    <div class="wood-backdrop" role="img" aria-label="Whitewashed wooden plank background"></div>
    <div class="side-band"></div>
    <div class="side-edge"></div>

    <header class="brand">
      <span class="brand-mark"></span>
      <div class="brand-name">VELQORITH</div>
    </header>

    <section class="intro">
      <p>At Velqorith we want to help you be the best you can be! That's why we have put together this simple guide to motivate, inspire, inform, and help you reach your goals.</p>
      <p>Below you will find a collection of healthy and easy recipe ideas and tips to kickstart your detox and diet journey.</p>
    </section>

    <svg class="headline" viewBox="0 0 848 1200" aria-label="Ready? Set.... Go!">
      <text class="ready" x="194" y="770" font-size="138" stroke-width="18" textLength="462" lengthAdjust="spacingAndGlyphs">READY?</text>
      <text class="set" x="192" y="912" font-size="182" stroke-width="22" textLength="450" lengthAdjust="spacingAndGlyphs">SET....</text>
      <text class="go" x="198" y="1062" font-size="150" stroke-width="20" textLength="280" lengthAdjust="spacingAndGlyphs">GO!</text>
    </svg>

    <div class="leaf-photo" role="img" aria-label="Photo of two fresh green leaves on a stem"></div>
  </main>
</body>
</html>
```